Letterhead design x 2, follower page, with compliments slip and envelope design X 2

Design letterhead x 2, follower page, with compliments slip and envelope x 2 for Harbor Venture Partners, a business broking company. Using the colours of the existing logo and a white background for a clean, sophisticated look.

Target Market(s)

Family Business owners and regular business owners looking to buy or sell their business, or improve the value of their business.

Font styles to use
Sans Serif

Requirements
Must have
• Letterhead design 1 - Additional logos for Crale Business Sales, NTQR and DWL to be included in a small size somewhere on the page. Crale Business Sales logo only to have the wording 'Powered By' alongside. Please do not distort the size of the logos.
Letterhead design 2 - Additional logos for NTQR and DWL to be included in a small size somewhere on the page. This design will not include the Crale Business Sales logo or the words 'Powered By'. Please do not distort the size of the logos.
Envelope design 1 - Please include an address window
Envelope design 2 - Do not include an address window

```html
<!DOCTYPE html>
<html lang="en">
<head>
<meta charset="utf-8">
<title>Harbor Venture Partners – Envelope Designs</title>
<link rel="stylesheet" href="https://fonts.googleapis.com/css2?family=Quicksand:wght@600&display=swap">
<style>
  :root {
    --page-bg: #e9eaea;
    --paper: #f4f5f5;
    --paper-edge: #dcdfdf;
    --brand-orange: #f0441a;
    --brand-grey: #6e7a82;
    --window-grey: #b4b9b9;
    --mosaic-dark: #c0623e;
    --mosaic-light: #d9b8a6;
  }
  html, body {
    margin: 0;
    width: 1200px;
    height: 900px;
    overflow: hidden;
    background: var(--page-bg);
  }
  .canvas {
    position: relative;
    width: 1200px;
    height: 900px;
  }
  .envelope {
    position: absolute;
    left: 210px;
    width: 780px;
    height: 390px;
    background: var(--paper);
    border: 1px solid var(--paper-edge);
    box-shadow: 0 10px 28px rgba(0, 0, 0, 0.12);
    overflow: hidden;
  }
  .envelope--window { top: 40px; }
  .envelope--plain { top: 470px; }

  .mosaic {
    position: absolute;
    top: 0;
    right: 0;
  }
  .mosaic--side {
    top: 200px;
    right: 0;
  }

  .brand {
    position: absolute;
    display: flex;
    align-items: center;
    font-family: "Quicksand", sans-serif;
    font-weight: 600;
    color: var(--brand-orange);
  }
  .brand__mark {
    flex: none;
    border-radius: 50%;
    border: 3px solid var(--brand-grey);
  }
  .brand__name {
    line-height: 1.05;
  }

  .envelope--window .brand {
    left: 60px;
    top: 110px;
    gap: 18px;
  }
  .envelope--window .brand__mark { width: 76px; height: 76px; }
  .envelope--window .brand__name { font-size: 34px; }

  .envelope--plain .brand {
    left: 44px;
    bottom: 40px;
    gap: 10px;
  }
  .envelope--plain .brand__mark { width: 38px; height: 38px; border-width: 2px; }
  .envelope--plain .brand__name { font-size: 15px; }

  .address-window {
    position: absolute;
    left: 420px;
    top: 210px;
    width: 300px;
    height: 110px;
    background: var(--window-grey);
  }
</style>
</head>
<body>
<main class="canvas">

  <section class="envelope envelope--window" aria-label="Envelope with address window">
    <svg class="mosaic" width="240" height="160" viewBox="0 0 240 160" role="img" aria-label="Mosaic of small copper squares fading toward the corner">
      <defs>
        <linearGradient id="mosaicFadeA" x1="1" y1="0" x2="0" y2="1">
          <stop offset="0" stop-color="var(--mosaic-dark)" stop-opacity="0.85"/>
          <stop offset="1" stop-color="var(--mosaic-light)" stop-opacity="0"/>
        </linearGradient>
      </defs>
      <polygon points="40,0 240,0 240,160" fill="url(#mosaicFadeA)"/>
    </svg>

    <div class="brand">
      <span class="brand__mark"></span>
      <span class="brand__name">Harbor<br>Venture<br>Partners</span>
    </div>

    <div class="address-window"></div>
  </section>

  <section class="envelope envelope--plain" aria-label="Envelope without address window">
    <svg class="mosaic" width="180" height="150" viewBox="0 0 180 150" role="img" aria-label="Mosaic of small copper squares in the top corner">
      <defs>
        <linearGradient id="mosaicFadeB" x1="1" y1="0" x2="0" y2="1">
          <stop offset="0" stop-color="var(--mosaic-dark)" stop-opacity="0.8"/>
          <stop offset="1" stop-color="var(--mosaic-light)" stop-opacity="0"/>
        </linearGradient>
      </defs>
      <polygon points="30,0 180,0 180,150" fill="url(#mosaicFadeB)"/>
    </svg>
    <svg class="mosaic mosaic--side" width="110" height="90" viewBox="0 0 110 90" role="img" aria-label="Small cluster of copper squares along the edge">
      <defs>
        <linearGradient id="mosaicFadeC" x1="1" y1="0.5" x2="0" y2="0.5">
          <stop offset="0" stop-color="var(--mosaic-dark)" stop-opacity="0.6"/>
          <stop offset="1" stop-color="var(--mosaic-light)" stop-opacity="0"/>
        </linearGradient>
      </defs>
      <rect x="0" y="0" width="110" height="90" fill="url(#mosaicFadeC)"/>
    </svg>

    <div class="brand">
      <span class="brand__mark"></span>
      <span class="brand__name">Harbor<br>Venture<br>Partners</span>
    </div>
  </section>

</main>
</body>
</html>
```